Velloro & Company - Tri-Fold Brochure
Tri-Fold Brochure
All Designers, Please Read:
I need to edit myself. Please ignore the previous post about the layout and use this one instead:
Outside 3 panels, from left to right:
panel 1 - CEO Quotes (let's title this section "What leaders say about us")
panel 2 - your choice - likely company contact information
panel 3 - cover art
Inside 3 panels:
panel 1 - About Velloro & Company, then What We Do
panel 2 - Adviser to CEOs, then Issues & Industries, then People & Values
panel 3 -- Miriam's bio (I know I need to cut out some copy to make this fit. Just put as much copy as you can for now while I figure out what to cut)
I really like the giant Vs in the cover art.
I can't wait to see the next round.
There are some good concepts here. Nice work, designers. Now that I've seen the layouts, here's what I'd like to see:
Outside 3 panels, from left to right (like #1 and #5):
panel 1 - Miriam's bio
panel 2 - Miriam's bio (continued)
panel 2 - People & Values, then Adviser to CEOs, then Issues & Industries
panel 3 -- ALL of the quotes from the CEOs in the "Results" section of my brief, but I like the title that one of you suggested "What leaders say about us"
I really like the way my bio is on the outer panels in #1. But I like the cover art for #2. Can we combine those two concepts for the outer three panels. Andd can I also see what the inside three panels would look like -- with all the relevant copy laid out: About Velloro & Company, People & Values, Advisor to CEOs, What We Do, Issues & Industries, Results. If you can lay it all out that way, I can see if I need to cut out some of the copy. But I need to see each of those sections on the inside panels.

```html
<!DOCTYPE html>
<html lang="en">
<head>
<meta charset="utf-8">
<title>Velloro &amp; Company – Tri-Fold Brochure</title>
<link rel="stylesheet" href="https://fonts.googleapis.com/css2?family=Open+Sans:wght@400;600;700&display=swap">
<style>
:root{
  --red:#c4161c;
  --red-deep:#8e0f13;
  --dark:#161616;
  --ink:#333333;
  --muted:#6f6f6f;
  --paper:#ffffff;
  --stage:#e6e4e1;
  --photo-a:#c9ced6;
  --photo-b:#6f7888;
}
*{box-sizing:border-box;margin:0;padding:0}
html,body{width:1200px;height:674px;overflow:hidden}
body{background:var(--stage);font-family:"Open Sans",Arial,sans-serif;color:var(--ink);position:relative}
.spread{position:absolute;top:117px;width:570px;height:440px;display:flex;box-shadow:0 4px 14px rgba(0,0,0,.25);background:var(--paper)}
.spread--outside{left:20px}
.spread--inside{left:610px}
.panel{position:relative;width:190px;height:440px;overflow:hidden}
.panel + .panel{border-left:1px solid #e2e2e2}

/* outside: quotes */
.quotes{padding:16px 14px}
.section-title{font-size:10px;font-weight:700;color:var(--red);text-transform:uppercase;letter-spacing:.3px;margin-bottom:8px}
.quote{font-size:6.4px;line-height:1.5;margin-bottom:9px;padding-left:7px;border-left:2px solid var(--red)}
.quote cite{display:block;font-style:normal;font-weight:700;color:var(--dark);margin-top:2px}

/* outside: contact */
.contact{background:var(--dark);color:#fff}
.contact-band{position:absolute;left:0;right:0;bottom:0;height:96px;background:var(--red);border-top:6px solid var(--red-deep)}
.contact-brand{position:absolute;top:140px;left:0;right:0;text-align:center}
.brand-mark{display:inline-block;width:26px;height:26px;background:var(--red);margin-bottom:8px}
.brand-name{font-size:12px;font-weight:700;color:#fff}
.contact-details{position:absolute;top:216px;left:0;right:0;text-align:center;font-size:6.6px;line-height:1.7}
.contact-phone{display:block;font-size:14px;font-weight:700;margin-bottom:4px}

/* outside: cover */
.cover-head{height:96px;display:flex;align-items:center;justify-content:center;gap:7px}
.cover-head .brand-mark{width:16px;height:16px;margin:0}
.cover-head .brand-name{color:var(--dark);font-size:12px}
.cover-photo{position:absolute;top:96px;left:0;right:0;height:240px;background:linear-gradient(160deg,var(--photo-a),var(--photo-b))}
.cover-band{position:absolute;left:0;right:0;top:336px;height:70px;background:var(--red);border-top:6px solid var(--red-deep)}
.cover-base{position:absolute;left:0;right:0;bottom:0;height:34px;background:var(--dark)}

/* inside: about */
.about-band{background:var(--dark);color:#fff;padding:14px 14px 10px}
.about-band .section-title{color:#fff;margin:0}
.body-copy{padding:10px 14px;font-size:6.4px;line-height:1.55}
.body-copy p{margin-bottom:6px}
.body-copy .section-title{margin:8px 0 5px}
.service-list{list-style:none;margin-bottom:6px}
.service-list li{padding-left:9px;position:relative;margin-bottom:2px}
.service-list li::before{content:"";position:absolute;left:0;top:2px;width:4px;height:4px;background:var(--red)}

/* inside: adviser */
.adviser{background:#f4f4f4;padding:16px 12px}
.feature{background:var(--paper);margin-bottom:12px;border-top:3px solid var(--red)}
.feature-title{background:var(--red);color:#fff;font-size:8px;font-weight:700;text-transform:uppercase;padding:5px 8px}
.feature p{font-size:6.4px;line-height:1.55;padding:7px 8px 9px}

/* inside: bio */
.bio{padding:16px 14px}
.bio-head{display:flex;align-items:center;gap:9px;margin-bottom:10px}
.bio-portrait{width:46px;height:46px;border-radius:50%;background:linear-gradient(160deg,var(--photo-a),var(--photo-b));border:2px solid var(--red);flex:none}
.bio-name{font-size:13px;font-weight:700;color:var(--red);line-height:1.1}
.bio-role{font-size:7px;font-weight:600;color:var(--dark)}
.bio p{font-size:6.4px;line-height:1.6;margin-bottom:7px}
.bio-footer{position:absolute;left:0;right:0;bottom:0;height:44px;background:var(--red);color:#fff;display:flex;align-items:center;justify-content:center;font-size:13px;font-weight:700}
</style>
</head>
<body>

<section class="spread spread--outside" aria-label="Brochure outside">
  <div class="panel quotes">
    <h2 class="section-title">What leaders say about us</h2>
    <p class="quote">“Their counsel helped our board see risks early and act with confidence during a difficult merger.”<cite>— Chief Executive, Regional Bank</cite></p>
    <p class="quote">“A rare partner who listens first, then tells you the truth you need to hear.”<cite>— Founder, Logistics Group</cite></p>
    <p class="quote">“We grew faster and with fewer surprises because their advice was practical and clear.”<cite>— President, Health Network</cite></p>
    <p class="quote">“Every session left our leadership team sharper, calmer and more aligned on what matters.”<cite>— CEO, Manufacturing Firm</cite></p>
  </div>

  <div class="panel contact">
    <div class="contact-brand">
      <span class="brand-mark"></span>
      <div class="brand-name">Velloro &amp; Company</div>
    </div>
    <div class="contact-details">
      <span class="contact-phone">555-014-2270</span>
      1200 Harbor Point Drive, Suite 400<br>
      Atlanta, GA 30305<br>
      jmarlow@velloroandco.com<br>
      www.velloroandco.com
    </div>
    <div class="contact-band"></div>
  </div>

  <div class="panel cover">
    <div class="cover-head">
      <span class="brand-mark"></span>
      <span class="brand-name">Velloro &amp; Company</span>
    </div>
    <div class="cover-photo" role="img" aria-label="Photo of smiling business people in suits"></div>
    <div class="cover-band"></div>
    <div class="cover-base"></div>
  </div>
</section>

<section class="spread spread--inside" aria-label="Brochure inside">
  <div class="panel">
    <div class="about-band"><h2 class="section-title">About Velloro &amp; Company</h2></div>
    <div class="body-copy">
      <p>Velloro &amp; Company advises chief executives and their teams on strategy, growth and leadership. We bring decades of hands-on experience to every engagement and stay with clients until the work is done.</p>
      <p>Our approach is discreet, direct and built on long-term trust with each leader we serve.</p>
      <h2 class="section-title">What We Do</h2>
      <p>We help leaders make better decisions, faster:</p>
      <ul class="service-list">
        <li>Strategic planning</li>
        <li>Executive coaching</li>
        <li>Board advisory</li>
        <li>Growth and transition</li>
        <li>Team alignment</li>
        <li>Crisis counsel</li>
      </ul>
      <p>Clients measure our value in clarity, momentum and results.</p>
    </div>
  </div>

  <div class="panel adviser">
    <div class="feature">
      <h3 class="feature-title">Adviser to CEOs</h3>
      <p>Leading a company can be lonely. We serve as a trusted sounding board for chief executives facing hard choices.</p>
    </div>
    <div class="feature">
      <h3 class="feature-title">Issues &amp; Industries</h3>
      <p>We work across finance, healthcare, technology, manufacturing and professional services on growth, succession and change.</p>
    </div>
    <div class="feature">
      <h3 class="feature-title">People &amp; Values</h3>
      <p>Integrity, candor and care guide how we work with every client and every team.</p>
    </div>
  </div>

  <div class="panel bio">
    <div class="bio-head">
      <div class="bio-portrait" role="img" aria-label="Portrait photo of Miriam Velloro"></div>
      <div>
        <h2 class="bio-name">Miriam Velloro</h2>
        <div class="bio-role">CEO &amp; Founder</div>
      </div>
    </div>
    <p>Miriam founded Velloro &amp; Company after two decades leading teams in finance and operations across growing firms.</p>
    <p>She has advised hundreds of chief executives on strategy, leadership and the personal demands of the top role.</p>
    <p>Clients value her calm judgment, plain speaking and deep commitment to their long-term success.</p>
    <p>Miriam serves on several nonprofit boards and speaks often on leadership and governance.</p>
    <div class="bio-footer">555-014-2270</div>
  </div>
</section>

</body>
</html>
```